Postcard Design for Direct Mail Campaign for PIttsburgh area attorney

I am an attorney in Pittsburgh, I did this before and selected three designs. I am not sure if those responding can see which three I selected. Those designs are in use now. All 3 go out. The issue is they cost the standard mailing rate and I will use all 3 of those forever. There will be times I would like to take advantage of the postcard mailing rate and thus this one is smaller. I want the postcard to emphasize I do criminal and SOME civil law. See my sites www.larvendefensecounsel.com and www.tobquill.net.

IN FACT I AM PUTTING THE THREE I AM MAILING RIGHT NOW IN THE IMAGES> I TRUST THAT THESE WILL BE USED TO INSPIRE AND GUIDE AND NO COPY. i Cannot upload those images. You can probably see my 3 winners.

Target Market(s)

Pittsburgh area people who may need a criminal attorney or a civil attorney.

Industry/Entity Type

Legal

Colors
ec1f27

Requirements
Must have
• A balanced criminal - civil thing as these are going to people in the mail with no envelope.
Nice to have
• On my site www.larvendefensecounsel.com I have badges in the sidebar.
Should not have
• People being arrested. I am putting up new images.

```html
<!DOCTYPE html>
<html lang="en">
<head>
<meta charset="utf-8">
<title>Postcard – Contact Side</title>
<link href="https://fonts.googleapis.com/css2?family=Figtree:wght@400;600;700&display=swap" rel="stylesheet">
<style>
  :root {
    --brand-red: #ee0000;
    --ink: #000000;
    --paper: #ffffff;
    --white: #ffffff;
    --rule: #8a8a8a;
  }
  * { margin: 0; padding: 0; box-sizing: border-box; }
  html, body {
    width: 1200px;
    height: 811px;
    overflow: hidden;
    background: var(--paper);
    font-family: "Figtree", Arial, sans-serif;
  }
  .postcard {
    position: relative;
    width: 1200px;
    height: 811px;
    background: var(--paper);
  }
  .contact-panel {
    position: absolute;
    left: 24px;
    top: 29px;
    width: 578px;
    height: 722px;
    background: var(--brand-red);
    color: var(--white);
  }
  .panel-tab {
    position: absolute;
    left: 0;
    top: 15px;
    width: 432px;
    height: 53px;
  }
  .panel-tab-label {
    position: absolute;
    left: 33px;
    top: 15px;
    height: 53px;
    line-height: 53px;
    font-size: 30px;
    font-weight: 700;
    color: var(--white);
    white-space: nowrap;
  }
  .office-block { position: absolute; left: 33px; top: 116px; }
  .office-name {
    font-size: 31px;
    font-weight: 700;
    line-height: 40px;
    white-space: nowrap;
  }
  .office-address, .office-phones {
    font-size: 23px;
    font-weight: 700;
    line-height: 32.5px;
  }
  .office-address { margin-top: 0; }
  .office-phones { margin-top: 32px; }
  .tagline-block { position: absolute; left: 37px; top: 384px; }
  .tagline {
    font-size: 32px;
    font-weight: 700;
    line-height: 40px;
    white-space: nowrap;
  }
  .tagline-details, .experience {
    font-size: 22px;
    font-weight: 700;
    line-height: 32px;
  }
  .experience { margin-top: 32px; }
  .bottom-band {
    position: absolute;
    left: 24px;
    top: 751px;
    width: 1153px;
    height: 22px;
    background: var(--ink);
  }
  .return-address {
    position: absolute;
    left: 641px;
    top: 58px;
    font-size: 13px;
    line-height: 18px;
    color: var(--ink);
  }
  .return-address .return-name { font-weight: 700; margin-bottom: 1px; }
  .postage-box {
    position: absolute;
    left: 1066px;
    top: 50px;
    width: 84px;
    height: 84px;
    border: 1px solid var(--rule);
    display: flex;
    align-items: center;
    justify-content: center;
    font-size: 13px;
    color: var(--ink);
    letter-spacing: 0.2px;
  }
</style>
</head>
<body>
<div class="postcard">
  <section class="contact-panel">
    <svg class="panel-tab" viewBox="0 0 432 53" aria-hidden="true">
      <polygon points="0,0 378,0 432,53 0,53" fill="#000000"/>
    </svg>
    <h2 class="panel-tab-label">Our Contact Details :</h2>

    <div class="office-block">
      <h1 class="office-name">The Law Office of Daniel K. Larven</h1>
      <p class="office-address">1800 Counsel Tower<br>512 Grant Street<br>Pittsburgh, PA 15219</p>
      <p class="office-phones">TEL: 412-555-0130 or 412-555-0162<br>FAX: 412-555-0187</p>
    </div>

    <div class="tagline-block">
      <h2 class="tagline">Competent Legal Representation</h2>
      <p class="tagline-details">Pittsburgh, Pennsylvania<br>412-555-0130</p>
      <p class="experience">Over 20 Years of Experience in<br>Criminal Defense , DUI Defense and<br>Personal Injury Cases<br>Serving all of Western PA</p>
    </div>
  </section>

  <address class="return-address" style="font-style: normal;">
    <div class="return-name">The Law Office of Daniel K. Larven</div>
    1800 Counsel Tower<br>512 Grant Street<br>Pittsburgh, PA 15219
  </address>

  <div class="postage-box">POSTAGE</div>

  <div class="bottom-band"></div>
</div>
</body>
</html>
```